Tidewell Consulting Schedule Of Rates

We need a brochure / proposal for our new company. Our company is a start up based in Australia who provides engineering and sales support to other renewable energy companies. Our brochure is a pitch-deck / sales item that catalogues our key services. We are engineering consultants.

Our website is www.tidewellpartners.com.au. Please review the website to get a feel of colour schemes etc.

We are looking for a strong, trustworthy feel, but the brochure also needs to be sales driven and to the point.

The second page that contains the $30 price point needs to be loud and clear.

The use of relevant icons throughout the document will be viewed favorably.

Please format the tables to look attractive.

The document will need to be in an editable format so content can be edited by us at a later date.

Please feel free to use the pics within the attached word document. The winning design will be provided with updated, clearer images upon request.

Thank you

Target Market(s)

Businesses that either sell or install solar PV and other renewable energy systems in Australia. Most of target market are likely to be electrical contractors.

Industry/Entity Type

Engineering

Colors
0255a3
0492cd
ffffff

Requirements
Must have
• Icons, graphics presentation, Clean and Clear, Business oriented. Sharp sales feel
Nice to have
• solar picture backgrounds maybe
Should not have
• cartoons, over sales driven,

```html
<!DOCTYPE html>
<html lang="en">
<head>
<meta charset="utf-8">
<title>Tidewell Consulting – Professional Panel Layout</title>
<link href="https://fonts.googleapis.com/css2?family=Dosis:wght@400;500;600;700&display=swap" rel="stylesheet">
<style>
  :root{
    --ink:#111111;
    --panel:#3b3b3d;
    --band:#0d0d0d;
    --light-text:#e6e6e6;
    --muted-text:#d2d2d2;
    --rule:#5a5a5c;
    --page-top:#ffffff;
    --page-side:#d9d9d9;
    --solar-blue:#3f5fb0;
    --solar-deep:#233c7a;
    --field-green:#8d8a2a;
  }
  *{box-sizing:border-box;margin:0;padding:0}
  html,body{width:848px;height:1200px;overflow:hidden}
  body{font-family:'Dosis',sans-serif;color:var(--ink);background:#fff}
  .sheet{position:relative;width:848px;height:1200px;overflow:hidden;
    background:linear-gradient(90deg,var(--page-side) 0%,var(--page-top) 22%,var(--page-top) 100%)}

  .intro{position:absolute;left:67px;top:72px}
  .intro-title{font-size:37px;font-weight:700;letter-spacing:.3px}
  .intro-list{list-style:none;margin-top:14px}
  .intro-list li{position:relative;padding-left:27px;font-size:29px;font-weight:500;color:#333;line-height:40px;letter-spacing:.4px}
  .intro-list li::before{content:"";position:absolute;left:2px;top:15px;width:13px;height:13px;border-radius:50%;background:var(--ink)}

  .band{position:absolute;left:0;width:848px;height:11px;background:var(--band)}
  .band-top{top:300px}
  .band-bottom{top:992px}

  .pricing{position:absolute;left:0;top:311px;width:848px;height:423px;background:var(--panel);color:var(--light-text)}
  .headline{position:absolute;left:60px;top:52px;width:390px;text-align:center}
  .headline-range{font-size:40px;font-weight:700;letter-spacing:1.5px;line-height:1}
  .headline-price{font-size:218px;font-weight:600;color:#fff;line-height:.8;margin-top:14px;letter-spacing:-2px}
  .headline-note{font-size:27px;font-weight:600;letter-spacing:1px;line-height:1;margin-top:18px}
  .headline-service{font-size:50px;font-weight:700;letter-spacing:1px;line-height:1;margin-top:6px}
  .divider{position:absolute;left:457px;top:45px;width:1px;height:332px;background:var(--rule)}
  .tiers{position:absolute;left:499px;top:53px;width:256px}
  .tier{padding-bottom:9px;margin-bottom:11px;border-bottom:1px solid var(--rule)}
  .tier:last-child{border-bottom:none}
  .tier-range{font-size:21px;font-weight:500;color:var(--muted-text);letter-spacing:.5px;line-height:1.2}
  .tier-price{font-size:25px;font-weight:700;color:#fff;letter-spacing:.5px;line-height:1.25}
  .tier-item{font-size:21px;font-weight:500;color:var(--muted-text);letter-spacing:.5px;line-height:1.2}

  .solar-field{position:absolute;left:0;top:734px;width:848px;height:258px;
    background:linear-gradient(170deg,var(--field-green) 0%,var(--solar-blue) 28%,var(--solar-deep) 100%)}

  .contact{position:absolute;left:47px;top:1071px;font-size:14.5px;line-height:21px;color:var(--ink);letter-spacing:.1px}
  .brand{position:absolute;left:538px;top:1078px;display:flex;align-items:center;gap:10px}
  .brand-mark{width:22px;height:22px;background:var(--ink)}
  .brand-name{font-size:34px;font-weight:700;color:var(--ink);letter-spacing:.2px}
</style>
</head>
<body>
<main class="sheet">
  <section class="intro">
    <h1 class="intro-title">Services – Professional Panel Layout</h1>
    <ul class="intro-list">
      <li>We can layout the panels for a small fee</li>
      <li>Clear &amp; Concise</li>
      <li>Ranging from 5kW – 300kW</li>
    </ul>
  </section>

  <div class="band band-top"></div>

  <section class="pricing">
    <div class="headline">
      <p class="headline-range">LESS THEN 30KW</p>
      <p class="headline-price">$30</p>
      <p class="headline-note">EX. GST SKYPLOT</p>
      <p class="headline-service">PANEL LAYOUT</p>
    </div>
    <div class="divider"></div>
    <div class="tiers">
      <div class="tier">
        <p class="tier-range">30KW - 100kW</p>
        <p class="tier-price">$80 Ex. Gst Skyplot</p>
        <p class="tier-item">Panel Layout</p>
      </div>
      <div class="tier">
        <p class="tier-range">101KW - 300kW</p>
        <p class="tier-price">$150 Ex. Gst Skyplot</p>
        <p class="tier-item">Panel Layout</p>
      </div>
      <div class="tier">
        <p class="tier-range">300KW + $360 Ex. Gst</p>
        <p class="tier-price">3D Drawings including</p>
        <p class="tier-item">shading analysis</p>
      </div>
    </div>
  </section>

  <div class="solar-field" role="img" aria-label="Aerial photograph of rows of blue solar panels across a grassy field"></div>

  <div class="band band-bottom"></div>

  <footer>
    <address class="contact" style="font-style:normal">
      P: 03 9016 4827 | M: 0400 318 672<br>
      E: sales@tidewellpartners.com.au<br>
      W: www.tidewellpartners.com.au
    </address>
    <div class="brand">
      <span class="brand-mark"></span>
      <span class="brand-name">Tidewell Consulting</span>
    </div>
  </footer>
</main>
</body>
</html>
```